Looking for awesome business card design with attached existing logo

We are a water, mold, and fire damage restoration company called "Torvane Seco" Looking for an awesome business card that is edgy yet professional and unique. Show me what you got!

```html
<!DOCTYPE html>
<html lang="en">
<head>
<meta charset="utf-8">
<title>Torvane Seco – Business Card</title>
<link href="https://fonts.googleapis.com/css2?family=Montserrat:wght@600;700&family=Lato:wght@400;700&display=swap" rel="stylesheet">
<style>
  :root{
    --stage:#1b1c1d;
    --teal:#2e4b57;
    --gold:#d6961f;
    --red:#c8192c;
    --paper:#ffffff;
    --ink:#2b3a40;
  }
  *{box-sizing:border-box;margin:0;padding:0}
  html,body{width:1200px;height:1122px;overflow:hidden;background:var(--stage)}
  .stage{position:relative;width:1200px;height:1122px}
  .card{position:absolute;left:220px;width:760px;height:434px;border-radius:26px;overflow:hidden}
  .card-front{top:90px;background:var(--teal);display:flex;align-items:center;justify-content:center}
  .wordmark{font-family:"Montserrat",sans-serif;font-weight:700;letter-spacing:1px;display:flex;align-items:center;gap:18px;white-space:nowrap}
  .wordmark-dot{width:16px;height:16px;border-radius:50%;background:var(--gold)}
  .card-front .wordmark{font-size:64px;color:var(--paper)}
  .card-back{top:598px;background:var(--paper)}
  .card-back .wordmark{position:absolute;right:48px;top:62px;font-size:40px;color:var(--teal);gap:12px}
  .card-back .wordmark-dot{width:11px;height:11px}
  .rule-long{position:absolute;left:380px;right:40px;top:152px;height:2px;background:var(--red)}
  .office{position:absolute;right:44px;top:170px;text-align:right;font-family:"Lato",sans-serif;color:var(--ink);font-size:17px;line-height:1.35}
  .office-name{font-weight:700;color:var(--teal);font-size:18px}
  .person{position:absolute;left:60px;top:206px;font-family:"Montserrat",sans-serif}
  .person-name{font-size:36px;font-weight:700;color:var(--teal);letter-spacing:.5px}
  .person-role{font-size:22px;font-weight:600;color:var(--gold);margin-top:2px}
  .rule-short{position:absolute;left:60px;top:300px;width:270px;height:2px;background:var(--red)}
  .contacts{position:absolute;left:60px;top:314px;list-style:none;font-family:"Lato",sans-serif;font-size:18px;color:var(--ink)}
  .contacts li{display:flex;align-items:center;gap:12px;height:24px}
  .contacts svg{width:16px;height:16px;flex:none}
  .footer{position:absolute;left:0;bottom:0;width:760px;height:100px}
  .website{position:absolute;right:40px;bottom:32px;font-family:"Lato",sans-serif;font-size:16px;letter-spacing:3px;color:var(--paper);white-space:nowrap}
</style>
</head>
<body>
<main class="stage">
  <section class="card card-front" aria-label="Card front">
    <div class="wordmark"><span class="wordmark-dot"></span>Torvane Seco</div>
  </section>

  <section class="card card-back" aria-label="Card back">
    <div class="wordmark"><span class="wordmark-dot"></span>Torvane Seco</div>
    <div class="rule-long"></div>
    <div class="office">
      <div class="office-name">Torvane Seco</div>
      <div>Your Address, City</div>
      <div>State, Zip 1235</div>
    </div>

    <div class="person">
      <div class="person-name">DANIEL HART</div>
      <div class="person-role">Founder &amp; CEO</div>
    </div>
    <div class="rule-short"></div>
    <ul class="contacts">
      <li><svg viewBox="0 0 16 16"><path fill="#d6961f" d="M3 1.5l2.5 0 1.2 3-1.6 1.2a8 8 0 0 0 5.2 5.2l1.2-1.6 3 1.2v2.5c0 .8-.7 1.5-1.5 1.5A12.5 12.5 0 0 1 1.5 3c0-.8.7-1.5 1.5-1.5z"/></svg>(555) 210-4386</li>
      <li><svg viewBox="0 0 16 16"><rect x="4" y="1" width="8" height="14" rx="1.5" fill="none" stroke="#d6961f" stroke-width="1.6"/><circle cx="8" cy="12.5" r=".9" fill="#d6961f"/></svg>(555) 210-4387</li>
      <li><svg viewBox="0 0 16 16"><rect x="1" y="3" width="14" height="10" rx="1" fill="#d6961f"/><path d="M1.5 3.8L8 9l6.5-5.2" fill="none" stroke="#fff" stroke-width="1.2"/></svg>office@torvaneseco.com</li>
    </ul>

    <svg class="footer" viewBox="0 0 760 100" preserveAspectRatio="none" aria-hidden="true">
      <path fill="#2e4b57" d="M0 86 L340 86 C372 86 370 20 410 20 L760 20 L760 100 L0 100 Z"/>
      <rect x="0" y="70" width="232" height="10" fill="#c8192c"/>
      <path fill="#d6961f" d="M238 72 L328 72 C342 72 346 58 350 48 L356 48 C352 62 346 80 328 80 L238 80 Z"/>
    </svg>
    <div class="website">WWW.TORVANESECO.COM</div>
  </section>
</main>
</body>
</html>
```